VORELLI Industrial Maintenance

I offer repair and maintenance services of industrial mechanics in Quebec. I would like a creation that reflects confidence, competence, professionalism and dynamism. I like the orange color and the blue color.

Target Market(s)

Industries and Manufacturing companies using industrial machinery for the manufacture of their products.

Industry/Entity Type

Manufacturing

Contact Information for Business Card

VORELLI Maintenance Industrielle
Tél: (450)-318-5907
Courriel: vorelli.mnt@brastomail.com

Font styles to use
Sans Serif

Colors
f78f20
0455a3

Requirements
Must have
• My company name: VORELLI Maintenance Industrielle My phone: (450) -318-5907 My email: vorelli.mnt@brastomail.com
Nice to have
• Integrate a representative logo of the mechanics (gears, mechanical parts)

```html
<!DOCTYPE html>
<html lang="fr">
<head>
<meta charset="utf-8">
<title>VORELLI Maintenance Industrielle – Business Card</title>
<link href="https://fonts.googleapis.com/css2?family=Lato:wght@400;700;900&display=swap" rel="stylesheet">
<style>
  :root {
    --blue: #0455a3;
    --orange: #f78f20;
    --white: #ffffff;
    --ink: #1a1a1a;
    --backdrop: #e9ebee;
  }
  * { box-sizing: border-box; margin: 0; padding: 0; }
  html, body {
    width: 1200px; height: 782px; overflow: hidden;
    background: var(--backdrop);
    font-family: "Lato", Arial, sans-serif;
  }
  .sheet {
    width: 1200px; height: 782px;
    display: flex; align-items: center; justify-content: center; gap: 40px;
  }
  .card {
    position: relative;
    width: 540px; height: 309px;
    overflow: hidden;
    box-shadow: 0 6px 18px rgba(0,0,0,0.18);
  }
  .card--back { background: var(--blue); }
  .card--front { background: var(--white); }

  .brand {
    display: flex; align-items: center; gap: 12px;
    font-weight: 900; text-transform: uppercase; line-height: 1.05;
  }
  .brand__mark {
    width: 44px; height: 44px; border-radius: 50%; flex: none;
  }
  .brand__name { font-size: 40px; letter-spacing: 3px; }
  .brand__tag { font-size: 14.5px; letter-spacing: 0.5px; display: block; }

  .card--back .brand {
    position: absolute; left: 50%; top: 50%;
    transform: translate(-50%, -50%);
    color: var(--white);
  }
  .card--back .brand__mark { background: var(--white); }

  .card--front .brand {
    position: absolute; right: 34px; top: 148px;
    color: var(--blue);
  }
  .card--front .brand__mark { background: var(--orange); width: 38px; height: 38px; }
  .card--front .brand__name { font-size: 34px; }
  .card--front .brand__tag { font-size: 12.5px; }

  .person { position: absolute; left: 30px; top: 30px; }
  .person__name {
    color: var(--blue); font-weight: 700; font-size: 19px;
    text-transform: uppercase; letter-spacing: 0.3px;
  }
  .person__role {
    color: var(--orange); font-size: 12.5px;
    text-transform: uppercase; margin-top: 2px;
  }

  .contact { position: absolute; left: 30px; top: 138px; list-style: none; }
  .contact__item {
    display: flex; align-items: center; gap: 8px;
    font-size: 15px; color: var(--ink); margin-bottom: 7px;
  }
  .contact__icon { width: 16px; height: 16px; flex: none; }

  .waves { position: absolute; left: 0; top: 0; width: 540px; height: 309px; }
</style>
</head>
<body>
<main class="sheet">

  <section class="card card--back" aria-label="Card back">
    <div class="brand">
      <span class="brand__mark" aria-hidden="true"></span>
      <span>
        <span class="brand__name">Vorelli</span>
        <span class="brand__tag">Maintenance Industrielle</span>
      </span>
    </div>
  </section>

  <section class="card card--front" aria-label="Card front">
    <svg class="waves" viewBox="0 0 540 309" aria-hidden="true">
      <path d="M0,168 C90,240 300,232 540,262 L540,292 C300,254 90,252 0,190 Z" fill="var(--orange)"/>
      <path d="M0,196 C90,258 300,262 540,300 L540,309 L0,309 Z" fill="var(--blue)"/>
    </svg>

    <div class="person">
      <p class="person__name">Lucien Tremblay</p>
      <p class="person__role">Managing Director</p>
    </div>

    <ul class="contact">
      <li class="contact__item">
        <svg class="contact__icon" viewBox="0 0 16 16" aria-hidden="true">
          <circle cx="8" cy="8" r="8" fill="var(--blue)"/>
          <path d="M5.2 4.2 L6.6 4 L7.3 5.9 L6.4 6.6 C6.9 7.7 7.9 8.7 9 9.2 L9.7 8.3 L11.6 9 L11.4 10.4 C8 10.6 5 7.6 5.2 4.2 Z" fill="var(--white)"/>
        </svg>
        (450) -318-5907
      </li>
      <li class="contact__item">
        <svg class="contact__icon" viewBox="0 0 16 16" aria-hidden="true">
          <circle cx="8" cy="8" r="8" fill="var(--blue)"/>
          <rect x="4" y="5" width="8" height="6" rx="0.8" fill="var(--white)"/>
          <path d="M4.3 5.4 L8 8.3 L11.7 5.4" stroke="var(--blue)" stroke-width="0.9" fill="none"/>
        </svg>
        vorelli.mnt@brastomail.com
      </li>
    </ul>

    <div class="brand">
      <span class="brand__mark" aria-hidden="true"></span>
      <span>
        <span class="brand__name">Vorelli</span>
        <span class="brand__tag">Maintenance Industrielle</span>
      </span>
    </div>
  </section>

</main>
</body>
</html>
```